Webdesign für Anbieter von Erotik-Geschichten
Zielgruppe
Wir sind ein Anbieter von Erotik-Geschichten. Die Marke heisst Lunvo Erotica. Das Erlebnis für die Kunden soll hochwertig und persönlich wirken. Daher in keiner Art und Weise schmuddelig. Die Zielgruppe sind Frauen ab ca. 20-40. Die Geschichten werden frei lesbar sein, d.h. es ist kein Online-Shop sondern mehr eine Art Blog mit verschiedenen Geschichten.
Aufgabenstellung
Wichtig ist uns eine schlichtes, minimalistisches Design (vrgl. Tafelwerk) aber trotzdem hochwertig (leicht luxuriös) wirkend.

```html
<!DOCTYPE html>
<html lang="de">
<head>
<meta charset="utf-8">
<title>Lunvo Erotica – Startseite</title>
<link rel="stylesheet" href="https://fonts.googleapis.com/css2?family=Karla:ital,wght@0,400;0,600;0,700;1,400&family=Playfair+Display:wght@400;500&display=swap">
<style>
:root{
  --bg:#ffffff;
  --topbar:#99948f;
  --ink:#1c1c1c;
  --muted:#6f6f6f;
  --footer:#262626;
  --footer-text:#dcdcdc;
  --bottom:#000000;
  --button-grey:#8f8c88;
  --required:#d23a3a;
}
*{box-sizing:border-box;margin:0;padding:0}
html,body{width:1200px;height:2400px;overflow:hidden;background:var(--bg)}
body{font-family:"Karla",Arial,sans-serif;color:var(--ink)}
.page{position:absolute;left:57px;top:0;width:1086px;height:2400px;background:var(--bg);box-shadow:0 0 4px rgba(0,0,0,.15)}
.abs{position:absolute}

/* top bar */
.topbar{left:0;top:0;width:1086px;height:30px;background:var(--topbar)}
.topbar .social{left:145px;top:9px;display:flex;gap:20px}
.topbar .social span{width:11px;height:11px;background:#fff;border-radius:2px;opacity:.9}
.topbar .contact{right:126px;top:8px;font-size:9px;color:#fff;display:flex;align-items:center;gap:4px}

/* header */
.header{left:0;top:30px;width:1086px;height:91px}
.brand{left:148px;top:22px;font-family:"Playfair Display",Georgia,serif;font-size:34px;color:var(--ink);display:flex;align-items:center;gap:10px}
.brand i{width:10px;height:10px;border-radius:50%;background:#c62a2a;display:block}
.nav{right:113px;top:38px;display:flex;gap:31px;font-size:15px;letter-spacing:.3px}
.nav .login{font-weight:600}

/* hero */
.hero{left:0;top:121px;width:1086px;height:472px;background:linear-gradient(180deg,#9c958c 0%,#d9c6ae 25%,#6f5f4c 45%,#8a6c52 65%,#4a3a2c 100%);color:#fff;text-align:center}
.hero .kicker{position:absolute;left:0;right:0;top:78px;font-size:10px;font-weight:700;letter-spacing:2px;color:#4a4a4a}
.hero h1{position:absolute;left:0;right:0;top:112px;font-family:"Playfair Display",Georgia,serif;font-weight:400;font-size:44px}
.hero h2{position:absolute;left:0;right:0;top:198px;font-family:"Playfair Display",Georgia,serif;font-weight:400;font-size:21px}
.hero p{position:absolute;left:368px;width:350px;top:255px;font-size:10.5px;line-height:20px;font-weight:600}
.hero .cta{position:absolute;left:480px;top:359px;width:171px;height:39px;background:#fff;color:#222;font-size:9.5px;font-weight:700;letter-spacing:1.3px;display:flex;align-items:center;justify-content:center}

/* categories */
.categories{left:110px;top:648px;font-size:15px;color:#444;line-height:24px;letter-spacing:.3px}
.categories .title{padding-left:5px}
.categories li{list-style:none;display:flex;align-items:center;gap:5px}
.categories li::before{content:"";width:7px;height:7px;border-radius:50%;background:#111}

/* story rows */
.row-label{left:110px;font-size:14px;font-weight:700;letter-spacing:.6px}
.story{width:133px}
.story .cover{width:133px;height:207px}
.story .caption{margin-top:12px;text-align:center;font-style:italic;font-size:16px;color:var(--muted)}
.cover.couple{background:linear-gradient(160deg,#3b2a20,#a47a5c 55%,#2a1e18)}
.cover.duo{background:linear-gradient(160deg,#1e1e20,#6a5a4a 50%,#151515)}
.cover.portrait{background:linear-gradient(180deg,#2a2a2a,#9a9a9a 45%,#3c3c3c)}
.cover.city{background:linear-gradient(180deg,#a9b8c2,#6b4d3a 45%,#2a2622)}

/* footer */
.footer{left:0;top:1762px;width:1086px;height:578px;background:var(--footer);color:var(--footer-text)}
.footer h3{position:absolute;font-family:"Playfair Display",Georgia,serif;font-weight:400;font-size:17px;letter-spacing:2.5px;color:#fff;line-height:22px}
.footer .address{left:117px;top:92px;font-size:10.5px;line-height:19px}
.footer .social{left:117px;top:200px;display:flex;gap:6px}
.footer .social span{width:28px;height:26px;background:#8b8987}
.form-label{position:absolute;left:419px;font-size:10.5px;font-weight:700;color:#fff;line-height:12px}
.form-label b{color:var(--required);font-weight:400}
.field{position:absolute;left:419px;background:#fff;border:1px solid #bbb}
.send{position:absolute;left:419px;top:341px;width:74px;height:28px;border-radius:6px;background:var(--button-grey);border:1px solid #bbb;color:#fff;font-size:12px;font-weight:700;display:flex;align-items:center;justify-content:center}
.legal{left:419px;top:398px;font-size:12px;line-height:38px;letter-spacing:.3px}
.bottom{left:0;top:2340px;width:1086px;height:60px;background:var(--bottom);color:#fff;text-align:center;font-size:14.5px;font-weight:700;line-height:19px;padding-top:11px}
</style>
</head>
<body>
<div class="page">

  <div class="abs topbar">
    <div class="abs social"><span></span><span></span><span></span></div>
    <div class="abs contact">
      <svg width="7" height="10" viewBox="0 0 7 10"><rect x=".5" y=".5" width="6" height="9" rx="1" fill="none" stroke="#fff"/></svg>
      999 999 999 &nbsp;|&nbsp;
      <svg width="10" height="9" viewBox="0 0 10 9"><path d="M.5 .5h9v6h-6l-2 2v-2h-1z" fill="none" stroke="#fff"/></svg>
      noreply@example.com
    </div>
  </div>

  <header class="abs header">
    <div class="abs brand">Lunvo<i></i></div>
    <nav class="abs nav">
      <span>Home</span><span>Geschichten</span><span>Über uns</span><span>Kontakt</span><span class="login">Login</span>
    </nav>
  </header>

  <section class="abs hero" role="img" aria-label="Paar am Seeufer bei Sonnenuntergang">
    <div class="kicker">LUNVO EROTICA</div>
    <h1>Lust auf mehr?</h1>
    <h2>Unsere Geschichten warten auf Sie</h2>
    <p>Faucibus in ornare quam viverra orci. Sapien pellentesque habitant morbi tristique senectus et netus. Nulla aliquet enim tortor at. Nunc consequat interdum varius sit.</p>
    <div class="cta">MEHR ENTDECKEN</div>
  </section>

  <ul class="abs categories">
    <div class="title">Produktkategorien</div>
    <li>Meistgelesene</li>
    <li>Neuerscheinungen</li>
    <li>Empfehlungen</li>
  </ul>

  <div class="abs row-label" style="top:790px">MEISTGELESENE</div>
  <div class="abs story" style="left:291px;top:790px"><div class="cover couple" role="img" aria-label="Titelbild: Paar in Umarmung"></div><div class="caption">Lorem ipsum</div></div>
  <div class="abs story" style="left:463px;top:790px"><div class="cover duo" role="img" aria-label="Titelbild: Paar im dunklen Raum"></div><div class="caption">Lorem ipsum</div></div>
  <div class="abs story" style="left:634px;top:790px"><div class="cover portrait" role="img" aria-label="Titelbild: Mann in Jeans, schwarz-weiß"></div><div class="caption">Lorem ipsum</div></div>
  <div class="abs story" style="left:808px;top:790px;width:140px"><div class="cover city" style="width:140px" role="img" aria-label="Titelbild: Straße zwischen Hochhäusern"></div><div class="caption">Lorem ipsum</div></div>

  <div class="abs row-label" style="top:1101px">NEUERSCHEINUNGEN</div>
  <div class="abs story" style="left:292px;top:1101px"><div class="cover couple" role="img" aria-label="Titelbild: Paar in Umarmung"></div><div class="caption">Lorem ipsum</div></div>
  <div class="abs story" style="left:476px;top:1101px"><div class="cover duo" role="img" aria-label="Titelbild: Paar im dunklen Raum"></div><div class="caption">Lorem ipsum</div></div>
  <div class="abs story" style="left:657px;top:1101px"><div class="cover portrait" role="img" aria-label="Titelbild: Mann in Jeans, schwarz-weiß"></div><div class="caption">Lorem ipsum</div></div>
  <div class="abs story" style="left:835px;top:1101px;width:140px"><div class="cover city" style="width:140px" role="img" aria-label="Titelbild: Straße zwischen Hochhäusern"></div><div class="caption">Lorem ipsum</div></div>

  <div class="abs row-label" style="top:1412px">EMPFEHLUNGEN</div>
  <div class="abs story" style="left:292px;top:1412px"><div class="cover couple" role="img" aria-label="Titelbild: Paar in Umarmung"></div><div class="caption">Lorem ipsum</div></div>
  <div class="abs story" style="left:476px;top:1412px"><div class="cover duo" role="img" aria-label="Titelbild: Paar im dunklen Raum"></div><div class="caption">Lorem ipsum</div></div>
  <div class="abs story" style="left:657px;top:1412px"><div class="cover portrait" role="img" aria-label="Titelbild: Mann in Jeans, schwarz-weiß"></div><div class="caption">Lorem ipsum</div></div>
  <div class="abs story" style="left:835px;top:1412px;width:140px"><div class="cover city" style="width:140px" role="img" aria-label="Titelbild: Straße zwischen Hochhäusern"></div><div class="caption">Lorem ipsum</div></div>

  <footer class="abs footer">
    <h3 style="left:117px;top:48px">Kontakt</h3>
    <div class="abs address">Lunvo Erotica<br>Musterstraße 90000<br>99999 Musterstadt<br>E-Mail: info@example.com<br>Telefonnummer: 999 999 999</div>
    <div class="abs social"><span></span><span></span><span></span></div>

    <h3 style="left:419px;top:56px">Schreiben Sie uns</h3>
    <div class="form-label" style="top:111px">Name <b>*</b></div>
    <div class="field" style="top:128px;width:330px;height:25px"></div>
    <div class="form-label" style="top:169px">Email <b>*</b></div>
    <div class="field" style="top:186px;width:330px;height:25px"></div>
    <div class="form-label" style="top:226px">Ihre Nachricht <b>*</b></div>
    <div class="field" style="top:243px;width:550px;height:83px"></div>
    <div class="send">Senden</div>

    <div class="abs legal">Impressum<br>Datenschutz<br>AGB<br>Liefer- und Zahlungsbedingungen</div>
  </footer>

  <div class="abs bottom">Home/Geschichten/Über uns/Kontakt<br>Copyright Lunvo 2021</div>
</div>
</body>
</html>
```